Skincare Cleanser Bottle Label

New product launch of a mint facial cleanser.
Brand is called Dorvelle.
Product will be called Lunara.
Looking for a label design that can be printed using silk screening.
High gloss white plastic bottle. 8oz. White push pump top.
Clinical skincare brand, professional image, sold in medical spas.

Target Market(s)

Women Age 20-65

Industry/Entity Type

Health And Wellness

Font styles to use
Serif
Sans Serif

Requirements
Must have
• Dorvelle brand name in the orignal font.
Should not have
• Multiple colours.

```html
<!DOCTYPE html>
<html lang="en">
<head>
<meta charset="utf-8">
<title>Dorvelle Lunara Mint Facial Cleanser Label</title>
<link href="https://fonts.googleapis.com/css2?family=Archivo+Narrow:wght@500&family=Josefin+Sans:wght@400&family=Lato:wght@400&display=swap" rel="stylesheet">
<style>
  :root {
    --page: #f4f4f4;
    --label: #ffffff;
    --band: #4a4a4a;
    --ink: #1a1a1a;
    --green: #3d8b37;
    --silver-light: #f7f7f7;
    --silver-mid: #d6d6d6;
    --silver-dark: #bdbdbd;
    --leaf-light: #6fbf4a;
    --leaf-dark: #2f7d2c;
  }
  html, body {
    margin: 0;
    padding: 0;
    width: 738px;
    height: 1200px;
    overflow: hidden;
    background: var(--page);
  }
  .canvas {
    position: relative;
    width: 738px;
    height: 1200px;
  }
  .label {
    position: absolute;
    left: 176px;
    top: 50px;
    width: 386px;
    height: 1100px;
    background: var(--label);
    box-shadow: 0 2px 10px rgba(0,0,0,0.08);
  }
  .top-band {
    position: absolute;
    left: 0; top: 0;
    width: 100%;
    height: 65px;
    background: var(--band);
  }
  .brand {
    position: absolute;
    top: 102px;
    left: 0; width: 100%;
    text-align: center;
    font-family: "Josefin Sans", sans-serif;
    font-size: 40px;
    letter-spacing: 1px;
    color: var(--ink);
    margin: 0;
  }
  .product-name {
    position: absolute;
    top: 212px;
    left: 58px;
    margin: 0;
    font-family: "Archivo Narrow", sans-serif;
    font-weight: 500;
    font-size: 74px;
    line-height: 1;
    color: var(--ink);
    text-decoration: underline;
    text-decoration-thickness: 3px;
    text-underline-offset: 8px;
  }
  .product-type {
    position: absolute;
    top: 395px;
    left: 49px;
    margin: 0;
    font-family: "Lato", sans-serif;
    font-weight: 400;
    font-size: 66px;
    line-height: 79px;
    color: var(--green);
  }
  .info-band {
    position: absolute;
    left: 0; top: 683px;
    width: 100%;
    height: 132px;
    background: linear-gradient(180deg, var(--silver-dark) 0%, var(--silver-light) 12%, var(--silver-mid) 45%, var(--silver-light) 80%, var(--silver-dark) 100%);
    display: flex;
    align-items: center;
    justify-content: center;
  }
  .info-text {
    margin: 0;
    width: 300px;
    text-align: center;
    font-family: "Josefin Sans", sans-serif;
    font-size: 14px;
    line-height: 27px;
    color: var(--ink);
  }
  .mint-leaf {
    position: absolute;
    left: 72px;
    top: 851px;
    width: 235px;
    height: 176px;
    border-radius: 50%;
    background: radial-gradient(ellipse at 50% 45%, var(--leaf-light) 0%, var(--leaf-dark) 70%, rgba(47,125,44,0) 100%);
  }
  .size {
    position: absolute;
    top: 1063px;
    left: 0; width: 100%;
    text-align: center;
    font-family: "Lato", sans-serif;
    font-size: 18px;
    color: var(--green);
    margin: 0;
  }
</style>
</head>
<body>
<div class="canvas">
  <section class="label">
    <div class="top-band"></div>
    <p class="brand">dorvelle</p>
    <h1 class="product-name">LUNARA</h1>
    <h2 class="product-type">Mint<br>Facial<br>Cleanser</h2>
    <div class="info-band">
      <p class="info-text">Lorem Ipsum is simply dummy text of the printing and typesetting industry. Lorem Ipsum has been the industry's standard dummy text ever since the 1500s.</p>
    </div>
    <div class="mint-leaf" role="img" aria-label="Sprig of fresh green mint leaves"></div>
    <p class="size">8 OZ</p>
  </section>
</div>
</body>
</html>
```